Personal Injury Lawyer Billboard

I would like a design created featuring the image of the lawyer centered in the middle of the design.
To the left of the lawyer's image it should read "INJURED?"
To the right of the lawyer's image, it should read "CALL DREW!"
Under Call Drew, include the phone number 318-555-0147.
At the bottom of the design include the lawyers information "Andrew Holloway Accident & Injury Lawyers"
PLEASE REMOVED THE BACKGROUND IMAGERY OF THE PHOTO SUBMITTED. Also, the colors for this design should match the colors shown in the logo (navy, white and relective soft gold). Please use those color combinations in ways that best stand out.

```html
<!DOCTYPE html>
<html lang="en">
<head>
<meta charset="utf-8">
<title>Injured? Call Drew – Andrew Holloway Accident &amp; Injury Lawyers</title>
<link rel="stylesheet" href="https://fonts.googleapis.com/css2?family=Anton&family=Archivo+Black&family=Oswald:wght@600&display=swap">
<style>
  :root {
    --navy: #00215f;
    --navy-soft: #1b2d6b;
    --white: #ffffff;
    --gold-dark: #a3811c;
    --gold-mid: #d4b33c;
    --gold-light: #fbe56f;
  }
  html, body {
    margin: 0;
    padding: 0;
    width: 1200px;
    height: 591px;
    overflow: hidden;
    background: var(--white);
  }
  .billboard {
    display: block;
    width: 1200px;
    height: 591px;
  }
  .headline-injured {
    font-family: "Oswald", "Arial Narrow", sans-serif;
    font-weight: 600;
    font-size: 195px;
    fill: var(--navy);
  }
  .headline-call {
    font-family: "Archivo Black", "Arial Black", sans-serif;
    font-size: 148px;
    fill: var(--navy);
  }
  .headline-name {
    font-family: "Archivo Black", "Arial Black", sans-serif;
    font-size: 175px;
    fill: url(#goldText);
  }
  .phone-number {
    font-family: "Anton", "Impact", sans-serif;
    font-size: 137px;
    fill: var(--white);
  }
  .firm-info {
    font-family: "Oswald", "Arial Narrow", sans-serif;
    font-weight: 600;
    fill: var(--white);
  }
  .firm-info-name { font-size: 46px; }
  .firm-info-practice { font-size: 25px; }
  .phone-icon { fill: var(--navy); }
  .navy-fill { fill: var(--navy); }
  .gold-fill { fill: url(#goldBand); }
</style>
</head>
<body>
<svg class="billboard" viewBox="0 0 1200 591" xmlns="http://www.w3.org/2000/svg">
  <defs>
    <linearGradient id="goldBand" x1="0" y1="0" x2="1" y2="0">
      <stop offset="0" stop-color="#a3811c"/>
      <stop offset="0.3" stop-color="#fbe56f"/>
      <stop offset="0.55" stop-color="#d4b33c"/>
      <stop offset="0.8" stop-color="#fbe56f"/>
      <stop offset="1" stop-color="#a3811c"/>
    </linearGradient>
    <linearGradient id="goldText" x1="0" y1="0" x2="1" y2="0">
      <stop offset="0" stop-color="#a3811c"/>
      <stop offset="0.5" stop-color="#fbe56f"/>
      <stop offset="1" stop-color="#a3811c"/>
    </linearGradient>
    <linearGradient id="portraitTone" x1="0" y1="0" x2="0" y2="1">
      <stop offset="0" stop-color="#6b5448"/>
      <stop offset="0.35" stop-color="#a77f69"/>
      <stop offset="0.55" stop-color="#1b2d6b"/>
      <stop offset="1" stop-color="#00215f"/>
    </linearGradient>
  </defs>

  <g class="background">
    <path class="navy-fill" d="M0,0 H1200 V82 C1000,40 750,22 560,28 C350,35 150,55 0,62 Z"/>
    <path class="gold-fill" d="M0,62 C150,55 350,35 560,28 C750,22 1000,40 1200,82 V100 C1000,58 750,45 560,50 C350,58 150,92 0,114 Z"/>
    <path class="gold-fill" d="M0,326 C220,322 420,340 640,372 V591 H0 Z"/>
    <path class="navy-fill" d="M0,377 C220,374 420,385 640,402 V591 H0 Z"/>
    <path class="gold-fill" d="M560,402 C800,398 1000,382 1200,345 V591 H560 Z"/>
  </g>

  <text class="headline-injured" x="44" y="291" textLength="434" lengthAdjust="spacingAndGlyphs">INJURED?</text>
  <text class="headline-call" x="713" y="193" textLength="275" lengthAdjust="spacingAndGlyphs">CALL</text>
  <g class="phone-icon" transform="translate(988,86) scale(4.2)">
    <path d="M6.62 10.79c1.44 2.830 3.76 5.14 6.59 6.59l2.2-2.2c.27-.27.67-.36 1.02-.24 1.12.37 2.33.57 3.57.57.55 0 1 .45 1 1V20c0 .55-.45 1-1 1-9.39 0-17-7.61-17-17 0-.55.45-1 1-1h3.5c.55 0 1 .45 1 1 0 1.25.2 2.45.57 3.57.11.35.03.74-.25 1.02l-2.2 2.2z"/>
    <path d="M19 12h2c0-4.970-4.03-9-9-9v2c3.87 0 7 3.13 7 7zm-4 0h2c0-2.76-2.24-5-5-5v2c1.66 0 3 1.34 3 3z"/>
  </g>
  <text class="headline-name" x="834" y="333" textLength="328" lengthAdjust="spacingAndGlyphs">DREW</text>

  <g class="lawyer-portrait" role="img" aria-label="Cut-out portrait of the smiling lawyer in a navy suit, white shirt and green tie, raising a fist">
    <path fill="url(#portraitTone)" d="M505,90 C505,40 560,18 590,18 C630,18 665,45 665,95 L665,215 C700,228 760,250 810,290 C840,330 855,400 853,430 L853,591 L385,591 L395,440 C400,360 410,320 440,300 C480,270 520,255 550,240 L515,200 C505,170 505,130 505,90 Z"/>
  </g>

  <g class="phone-panel">
    <rect x="488" y="429" width="656" height="180" rx="18" fill="#ffffff"/>
    <rect x="498" y="438" width="636" height="170" rx="12" class="navy-fill"/>
    <text class="phone-number" x="519" y="559" textLength="594" lengthAdjust="spacingAndGlyphs">318-555-0147</text>
  </g>

  <g class="firm-info">
    <text class="firm-info-name" x="68" y="482">ANDREW HOLLOWAY</text>
    <text class="firm-info-practice" x="68" y="520">ACCIDENT &amp; INJURY LAWYERS</text>
  </g>
</svg>
</body>
</html>
```